County Surplus Auction

This postcard is advertising the upcoming Brindle County Surplus Equipment Auction we are conducting. The auction will be online only and will open on Monday, June 1 at 11:00 a.m. and close on Tuesday, June 2 at 2:00 p.m. Advertise our website www.tkvbids.example and our phone number 770-555-0147 very visibly, and this license number has to be included, but does not need to be very large GA Firm Lic #C7316. Please also advertise pre-auction viewing dates of Thursday, May 28 and Friday May 29, 11:00 a.m. until 3:00 p.m. both days.

```html
<!DOCTYPE html>
<html lang="en">
<head>
<meta charset="utf-8">
<title>Brindle County Surplus Equipment Online Auction – Postcard</title>
<link href="https://fonts.googleapis.com/css2?family=Source+Sans+3:ital,wght@0,400;0,600;0,700;1,600;1,700&display=swap" rel="stylesheet">
<style>
  :root{
    --gold:#ad8c2c;
    --gold-light:#d9c38a;
    --gold-pale:#efe3c3;
    --brown:#3a1f12;
    --accent-brown:#8a5a2a;
    --white:#ffffff;
    --page:#ece8df;
    --rule:#b9b9b9;
  }
  *{box-sizing:border-box;margin:0;padding:0}
  html,body{width:1109px;height:1200px;overflow:hidden}
  body{background:var(--page);font-family:"Source Sans 3",Arial,sans-serif;color:var(--brown);position:relative}
  .card{position:absolute;background:var(--white);overflow:hidden}
  .card--front{left:68px;top:48px;width:812px;height:527px}
  .card--back{left:229px;top:625px;width:808px;height:523px}
  .abs{position:absolute}
  .photo{position:absolute}
  .header-band{position:absolute;background:var(--gold);color:var(--white);text-align:center}
  .title{font-weight:600;line-height:1}
  .subtitle{font-weight:700;color:var(--brown);letter-spacing:2px;line-height:1}
  .dates{font-weight:700;text-decoration:underline;text-underline-offset:4px;text-decoration-thickness:2px;text-align:center;line-height:33px}
  .viewing{font-style:italic;font-weight:600;color:var(--accent-brown)}
  .contact{font-style:italic;font-weight:700;color:var(--brown);display:flex;align-items:center;gap:8px;white-space:nowrap}
  .license{font-style:italic;font-size:12px;color:var(--brown)}
  .waves{position:absolute;left:0;bottom:0}
</style>
</head>
<body>

<section class="card card--front">
  <div class="photo" role="img" aria-label="Hand holding a gavel reaching out of a laptop screen" style="left:12px;top:2px;width:162px;height:113px;background:radial-gradient(ellipse at 45% 45%,#8fa9c9 0%,#c9d2dc 45%,#f4f4f4 80%)"></div>
  <div class="header-band" style="left:174px;top:2px;width:638px;height:113px">
    <div class="title" style="font-size:36px;margin-top:22px">Brindle County Surplus Equipment</div>
    <div class="subtitle" style="font-size:34px;margin-top:10px">ONLINE AUCTION</div>
  </div>

  <div class="photo" role="img" aria-label="Red farm tractor on a gravel lot" style="left:1px;top:130px;width:255px;height:179px;background:linear-gradient(180deg,#a9c6e4 0%,#8ea07a 35%,#9a4a3c 60%,#6d6b66 100%)"></div>
  <div class="photo" role="img" aria-label="Red sedan parked among surplus vehicles" style="left:265px;top:130px;width:267px;height:179px;background:linear-gradient(180deg,#b9d2ea 0%,#c4c6c4 35%,#a8283a 62%,#8d8a84 100%)"></div>
  <div class="photo" role="img" aria-label="Camouflage military crane truck" style="left:541px;top:130px;width:270px;height:179px;background:linear-gradient(180deg,#7fa9d8 0%,#b8c6a0 35%,#7a7d52 65%,#4f4f4c 100%)"></div>

  <p class="dates abs" style="left:0;top:326px;width:812px;font-size:25px">The auction will be online only and will open on Monday,<br>June 1 at 11:00 a.m. and close on Tuesday, June 2 at 2:00 p.m</p>
  <p class="viewing abs" style="left:0;top:397px;width:812px;text-align:center;font-size:16px;line-height:22px">Pre-auction viewing dates: Thursday, May 28 and Friday, May 29,<br>11:00 a.m. until 3:00 p.m. both days.</p>

  <svg class="waves" width="812" height="90" viewBox="0 0 812 90" aria-hidden="true">
    <path d="M0 10 C220 -8 470 40 812 12 L812 90 L0 90 Z" fill="var(--gold-pale)"/>
    <path d="M0 22 C230 6 480 50 812 26 L812 90 L0 90 Z" fill="var(--gold-light)"/>
    <path d="M0 72 C260 52 520 92 812 58 L812 90 L0 90 Z" fill="var(--gold)"/>
  </svg>
  <div class="contact abs" style="left:18px;top:460px;font-size:31px">
    <svg width="40" height="40" viewBox="0 0 40 40" aria-hidden="true"><circle cx="20" cy="20" r="17" fill="none" stroke="var(--brown)" stroke-width="3"/><path d="M13 11c2-1 3 0 4 3l1 2c0 1-1 2-2 3 1 3 3 5 6 6 1-1 2-2 3-2l2 1c3 1 4 2 3 4-1 2-3 3-5 3-7-1-13-7-14-14 0-3 1-5 2-6z" fill="var(--brown)"/></svg>
    <span>770-555-0147</span>
  </div>
  <div class="contact abs" style="right:22px;top:462px;font-size:31px">www.tkvbids.example</div>
  <div class="license abs" style="right:26px;top:495px">GA Firm Lic #C7316</div>
</section>

<section class="card card--back">
  <div class="header-band" style="left:0;top:0;width:498px;height:113px">
    <div class="title" style="font-size:25px;margin-top:24px">Brindle County Surplus Equipment</div>
    <div class="subtitle" style="font-size:24px;margin-top:22px">ONLINE AUCTION</div>
  </div>
  <div class="abs" style="left:686px;top:28px;width:105px;height:84px;border:1px solid #9a9a9a"></div>
  <div class="abs" style="left:502px;top:130px;width:1px;height:310px;background:var(--rule)"></div>
  <div class="abs" style="left:539px;top:264px;width:254px;height:1px;background:var(--rule)"></div>
  <div class="abs" style="left:539px;top:312px;width:254px;height:1px;background:var(--rule)"></div>
  <div class="abs" style="left:539px;top:359px;width:254px;height:1px;background:var(--rule)"></div>

  <p class="abs" style="left:17px;top:140px;font-size:22px;font-weight:600;line-height:28.5px">The auction will be online only and will<br>open on Monday, June 1 at 11:00 a.m.<br>and close on Tuesday, June 2 at 2:00 p.m</p>
  <p class="viewing abs" style="left:17px;top:247px;font-size:16px;line-height:22px">Pre-auction viewing dates:<br>Thursday, May 28 and Friday, May 29,<br>11:00 a.m. until 3:00 p.m. both days.</p>

  <div class="photo" role="img" aria-label="Hand holding a gavel reaching out of a laptop screen" style="left:269px;top:287px;width:207px;height:128px;background:radial-gradient(ellipse at 55% 45%,#8fa9c9 0%,#c9d2dc 45%,#ffffff 80%)"></div>

  <div class="contact abs" style="left:22px;top:340px;font-size:29px">www.tkvbids.example</div>
  <div class="contact abs" style="left:20px;top:385px;font-size:30px">
    <svg width="40" height="40" viewBox="0 0 40 40" aria-hidden="true"><circle cx="20" cy="20" r="17" fill="none" stroke="var(--brown)" stroke-width="3"/><path d="M13 11c2-1 3 0 4 3l1 2c0 1-1 2-2 3 1 3 3 5 6 6 1-1 2-2 3-2l2 1c3 1 4 2 3 4-1 2-3 3-5 3-7-1-13-7-14-14 0-3 1-5 2-6z" fill="var(--brown)"/></svg>
    <span>770-555-0147</span>
  </div>

  <svg class="waves" width="808" height="86" viewBox="0 0 808 86" aria-hidden="true">
    <path d="M0 10 C230 -6 480 34 808 4 L808 86 L0 86 Z" fill="var(--gold-pale)"/>
    <path d="M0 24 C240 8 500 44 808 18 L808 86 L0 86 Z" fill="var(--gold-light)"/>
    <path d="M0 66 C260 48 520 86 808 52 L808 86 L0 86 Z" fill="var(--gold)"/>
  </svg>
</section>

</body>
</html>
```